NO MORE DESIGNS PLEASE."OPENING SOON' brochure for BRIGHTCELL ACCUMULATORS Pty Ltd .

Brightcell Accumulators is a locally owed and operated company. We provide a quality range of batteries (Halvex LiFeP04 and Quenstrom). From traditional sealed lead acid batteries, the latest AGM technologies and Lithium iron phosphate (LiFeP04).Our Suppliers have been in the manufacturing and battery industry for over 40 years. We wholesale and retail from a modern warehouse in Butler WA. We supply batteries for most applications including , Automotive, Critical power, Fire and Security, Mobility, Marine, Powersport, Motorcycle, Recreation, and truck and Tractor. All our Lithium iron phosphate (LiFeP04) batteries are IEC certified which sets us apart from other inferior products on the market. We are a start up business and new to the area. This brochure is to let people know we are opening soon, where we are and what we do.As part of our service we offer free delivery free battery testing and diagnosis and free installation. WE HAVE 3 DESIGNS WE ARE CHOOSING FROM FOR OUR WINNER. THANKYOU TO ALL THE TALENTED DESIGNERS THAT HAVE BLESSED US WITH THERE CREATIONS. IT IS VERY DIFFICULT TO TURN AWAY SUCH FANTASTIC TALENT. WE CAN ONLY CHOOSE ONE . THANKYOU FOR UNDERSTANDING.

Target Market(s)

18-65

Industry/Entity Type

Automotive

Font styles to use
Sans Serif

Colors
0392cd
f5f5f5
b1b1b1

Requirements
Must have
• WE HAVE 3 DESIGNS WE ARE CHOOSING FROM FOR OUR WINNER. THANKYOU TO ALL THE TALENTED DESIGNERS THAT HAVE BLESSED US WITH THERE CREATIONS. IT IS VERY DIFFICULT TO TURN AWAY SUCH FANTASTIC TALENT. WE CAN ONLY ONE. THANKYOU FOR UNDERSTANDING.
Nice to have
• Some wow factor
Should not have
• Boxes and lines

```html
<!DOCTYPE html>
<html lang="en">
<head>
<meta charset="utf-8">
<title>Brightcell Accumulators – Opening Soon</title>
<link rel="stylesheet" href="https://fonts.googleapis.com/css2?family=Bebas+Neue&family=Open+Sans:wght@400;700&display=swap">
<style>
  :root {
    --sky-top: #0b2a78;
    --sky-bottom: #1f6cf2;
    --frame: #ffffff;
    --cloth-light: #f5f5f5;
    --cloth-shade: #d9dadd;
    --headline: #3fb0ec;
    --headline-shadow: #8a97a6;
    --brand: #3a6ed2;
    --battery: #0f2f63;
    --copy: #ffffff;
    --offer: #d2171c;
  }
  * { margin: 0; padding: 0; box-sizing: border-box; }
  html, body { width: 848px; height: 1200px; overflow: hidden; background: #ffffff; }
  .brochure {
    position: relative;
    width: 848px;
    height: 1200px;
    overflow: hidden;
    background: linear-gradient(180deg, var(--sky-top) 0%, #134ab8 45%, var(--sky-bottom) 100%);
    font-family: "Open Sans", sans-serif;
  }
  .frame {
    position: absolute;
    inset: 8px;
    border: 3px solid var(--frame);
    pointer-events: none;
  }
  .hang-cords { position: absolute; left: 0; top: 0; width: 848px; height: 140px; }
  .banner {
    position: absolute;
    left: 171px;
    top: 93px;
    width: 527px;
    height: 680px;
    background: linear-gradient(180deg, var(--cloth-light) 0%, #eeeff1 60%, var(--cloth-shade) 100%);
    box-shadow: 0 10px 30px rgba(0, 0, 0, 0.25);
  }
  .brand {
    position: absolute;
    left: 0;
    right: 0;
    top: 192px;
    display: flex;
    justify-content: center;
    align-items: center;
    gap: 10px;
    color: var(--brand);
    font-family: "Open Sans", sans-serif;
    font-weight: 700;
    font-size: 21px;
    letter-spacing: 1px;
  }
  .brand-square { width: 26px; height: 26px; background: var(--brand); }
  .headline {
    position: absolute;
    left: 0;
    right: 0;
    top: 300px;
    text-align: center;
    font-family: "Bebas Neue", sans-serif;
    font-size: 158px;
    line-height: 126px;
    color: var(--headline);
    text-shadow: 3px 4px 0 var(--headline-shadow);
  }
  .battery {
    position: absolute;
    left: 296px;
    top: 613px;
    width: 274px;
    height: 225px;
    background: linear-gradient(180deg, #2a5b8f 0%, var(--battery) 18%, var(--battery) 100%);
  }
  .battery-shadow {
    position: absolute;
    left: 250px;
    top: 828px;
    width: 366px;
    height: 22px;
    border-radius: 50%;
    background: radial-gradient(ellipse at center, rgba(0, 0, 0, 0.35), rgba(0, 0, 0, 0));
  }
  .about {
    position: absolute;
    left: 170px;
    width: 508px;
    top: 914px;
    text-align: center;
    color: var(--copy);
    font-size: 15.5px;
    line-height: 21px;
  }
  .about p + p { margin-top: 12px; padding: 0 40px; }
  .offer-strip {
    position: absolute;
    left: 0;
    right: 0;
    top: 1088px;
    height: 34px;
    background: var(--frame);
    display: flex;
    align-items: center;
    justify-content: center;
    color: var(--offer);
    font-size: 16px;
  }
</style>
</head>
<body>
<main class="brochure">
  <svg class="hang-cords" viewBox="0 0 848 140" aria-hidden="true">
    <line x1="0" y1="40" x2="173" y2="95" stroke="#dfe3ea" stroke-width="3"/>
    <line x1="848" y1="40" x2="696" y2="95" stroke="#dfe3ea" stroke-width="3"/>
  </svg>
  <div class="banner" role="img" aria-label="Hanging white cloth banner with soft folds"></div>
  <div class="brand"><span class="brand-square"></span>BRIGHTCELL ACCUMULATORS</div>
  <h1 class="headline">OPENING<br>SOON</h1>
  <div class="battery-shadow"></div>
  <div class="battery" role="img" aria-label="Navy car battery with red and blue terminals and a yellow lightning bolt"></div>
  <section class="about">
    <p>We supply batteries for Automotive, Critical power, Fire and Security, Mobility, Marine, Powersport, Motorcycle, Recreation, and truck and Tractor.</p>
    <p>Our suppliers have been in the manufacturing and battery industry for over 40 years.</p>
  </section>
  <div class="offer-strip">Free Delivery Free battery testing and diagnosis and free installation.</div>
  <div class="frame"></div>
</main>
</body>
</html>
```